The Hearth Guard Expert needs a Wordpress site for Home, Life and Safety Emergencies

NEED CUSTOM THEME FILES FOR WORDPRESS ncluded. I need a wordpress website that I will be able to edit down the road. Content wise the site I was trying to build is accurate. http://www.hearthguardexpert.example The site focuses on life, safety and home emergencies. My target audience is the first time home buyer. Usually in mid 20's think engineering type person.

I am up for a complete redesign. I want it to look clean and neat.

Things I need to have on the site :

- 2 Menus - A main menu and a secondary menu at top of page
- Search Bar in one of the main menus
- Social Media Share Buttons on one of the menus
- I am up for a color change (Maybe something a little softer) Need Help
- Main Page should be set up as a main page with separate blog page
- Need a CTA / Sign up for newsletter on page (location can vary)
- Blog Categories: When clicked need to show the full article and image.
- If you click on my home safety you will see how they are set up as a grid. I do not like this I want them to be easy to read and flow in order.

The site is going to mainly provide information for First Time Home Buyers. Eventually a page will be set up to sign up for a paid Home Safety Course. For now I want to focus on the content.

Mail should function with mail chimp for now.
This needs to be a functioning theme that I can edit. I currently have the rights to divi builder if that helps. I don't want to have to worry about the site I just want to focus on content creation.

Thank you

Target Market(s)

First Time Home Buyers Usually person in their 20's or 30's. Someone of the engineering, legal aid type mindset.

Industry/Entity Type

Safety

Coding

Coded - Design and coding required

Font styles to use
Serif
Sans Serif
Script

Colors

Designer to choose colors to be used in the design.

Requirements
Must have
• Wordpress integration.
• 2 Menus on top - Main and secondary
• Search function in a menu
• Social Media Icons in menu
• Sidebar with image of myself and some info on top , posts , categories
• Categories of blog posts need to list on the page. Not grid.
• Email signup on page at some part. (can be bottom, top or side. )
• Nice Clean state Front page.
• Color Combination that works well. (Doesn't have to be what is their now)
• Current links to site.
• Learn CPR needs to be a link to an external site ( http://www.rescueskillsnorthvale.example)
Nice to have
• I am flexible on the main page site design. I am not good at this so anything you feel. I cannot describe what I want but I will know it when I see it.
• I will come up with the information. Of course if any copy could be provided and shows value I would be willing to pay extra.
Should not have
• Grid Style for blog posts.
• Blog Posts should be in list style and each post for each category will just go down the page by order of date posted.

```html
<!DOCTYPE html>
<html lang="en">
<head>
<meta charset="utf-8">
<title>The Hearth Guard Expert</title>
<link href="https://fonts.googleapis.com/css2?family=Lato:ital,wght@0,400;0,700;0,900;1,700&display=swap" rel="stylesheet">
<style>
:root{
  --red:#ec2227;
  --brown:#5a2d0c;
  --ink:#222;
  --grey:#555;
  --light:#cfcfcf;
  --black:#000;
  --white:#fff;
}
*{box-sizing:border-box;margin:0;padding:0}
html,body{width:715px;height:1200px;overflow:hidden}
body{font-family:'Lato',sans-serif;color:var(--ink);background:var(--white)}
a{color:inherit;text-decoration:none}
ul{list-style:none}
.wrap{padding:0 47px}

/* top bar */
.topbar{height:25px;background:var(--red);display:flex;align-items:center;justify-content:space-between}
.topbar .secondary-menu{display:flex;gap:19px;font-size:10px;color:var(--white)}
.topbar .tools{display:flex;align-items:center;gap:12px}
.search{width:117px;height:18px;border:1px solid var(--white);border-radius:10px;display:flex;align-items:center;justify-content:space-between;padding:0 7px;font-size:9px;color:var(--white)}
.social{display:flex;gap:9px}
.social span{width:10px;height:10px;border-radius:50%;background:var(--white);display:block}

/* header */
.site-header{height:50px;display:flex;align-items:center;justify-content:space-between}
.brand-name{font-weight:900;font-size:17px;color:var(--brown);line-height:1.1}
.brand-tag{font-size:9px;color:var(--red);margin-top:2px}
.main-menu{display:flex;gap:12px;font-size:10.5px;color:var(--grey);height:50px;align-items:center}
.main-menu .active{color:var(--red);height:50px;display:flex;align-items:center;border-bottom:2px solid var(--red)}

/* hero */
.hero{height:341px;position:relative;background:
  radial-gradient(ellipse at 60% 40%,#f4a52a 0%,#d8621a 35%,#7a2a0c 70%,#2a120a 100%)}
.hero-text{position:absolute;left:47px;top:48px}
.hero h1{font-size:24px;font-weight:700;color:var(--white);line-height:1.05;width:260px}
.btn-signup{display:inline-block;margin-top:18px;background:var(--white);color:var(--ink);font-size:12px;padding:8px 14px;border-radius:16px}

/* intro */
.intro{height:229px;padding-top:31px}
.intro h2{text-align:center;font-size:14px;font-weight:700;text-transform:uppercase;line-height:1.3;padding:0 15px}
.intro-cols{display:flex;justify-content:space-between;margin-top:24px;align-items:flex-start}
.facts{width:225px;color:var(--red);font-size:9.5px;font-weight:700;line-height:1.55;list-style:disc;padding-left:9px}
.intro-brand{width:160px;text-align:center;padding-top:4px}
.intro-brand .mark{width:58px;height:58px;border:3px solid var(--red);margin:0 auto 8px}
.intro-brand .name{font-weight:900;font-size:14px;color:var(--brown);line-height:1.15}
.intro-brand .tag{font-size:8px;color:var(--red);margin-top:3px}
.promise{width:215px;font-size:9.5px;color:var(--grey);line-height:1.55;list-style:disc;padding-left:9px;margin-top:-6px}

/* safety info */
.safety{height:213px;background:var(--black);padding-top:30px}
.safety h2{text-align:center;font-size:24px;font-weight:700;color:var(--white)}
.safety h2 span{color:var(--red)}
.topics{display:flex;justify-content:space-between;margin-top:20px;padding:0 42px}
.topic{width:90px;text-align:center;color:var(--white);font-size:13px;font-weight:700}
.topic .circle{width:74px;height:74px;border-radius:50%;background:var(--red);margin:0 auto 9px;display:flex;align-items:center;justify-content:center}

/* mailing */
.mailing{height:190px;background:var(--red);padding-top:29px;text-align:center}
.mailing h2{font-size:24px;font-weight:700;color:var(--black)}
.mailing h2 span{color:var(--white)}
.mailing p{font-size:9.5px;color:var(--white);line-height:1.55;width:465px;margin:8px auto 0}
.signup-form{display:flex;align-items:center;gap:7px;margin-top:26px}
.field{width:168px;height:28px;background:var(--white);border:1px solid #ddd;font-size:9.5px;color:var(--grey);text-align:left;padding:8px 6px}
.btn-subscribe{margin-left:6px;width:93px;height:30px;border-radius:15px;background:var(--black);color:var(--white);font-size:12px;display:flex;align-items:center;justify-content:center}

/* footer */
.footer{height:124px}
.footer-menu{display:flex;gap:19px;font-size:9px;color:var(--grey);height:46px;align-items:center;border-bottom:1px solid var(--light)}
.footer h3{font-size:13px;font-weight:700;margin:10px 0 0 3px}
.footer h3 span{color:var(--red)}
.contacts{display:flex;justify-content:space-between;margin-top:8px}
.contact{display:flex;align-items:center;gap:8px;font-size:9px;color:var(--grey);line-height:1.45;flex:none;white-space:nowrap}
.contact .ico{width:25px;height:25px;border-radius:50%;background:#d8d8d8;flex:none;display:flex;align-items:center;justify-content:center}
.contact .ico.dark{background:var(--black)}
.bottombar{height:28px;background:var(--red);display:flex;align-items:center;justify-content:space-between;color:var(--white);font-size:10px}
.bottombar .legal{display:flex}
.bottombar .legal a{padding:0 12px;border-left:1px solid var(--white)}
.bottombar .legal a:first-child{border:none}
.bottombar .legal a:last-child{padding-right:0}
</style>
</head>
<body>

<div class="topbar wrap">
  <ul class="secondary-menu">
    <li><a href="#">Home Safety</a></li>
    <li><a href="#">Life Safety</a></li>
    <li><a href="#">Fire Safety</a></li>
    <li><a href="#">Pet Safety</a></li>
    <li><a href="#">Safety Saturday</a></li>
  </ul>
  <div class="tools">
    <div class="search">Search here...
      <svg width="9" height="9" viewBox="0 0 10 10"><circle cx="4" cy="4" r="3" fill="none" stroke="#fff" stroke-width="1.6"/><line x1="6.2" y1="6.2" x2="9" y2="9" stroke="#fff" stroke-width="1.8"/></svg>
    </div>
    <div class="social">
      <span aria-label="Social link 1"></span><span aria-label="Social link 2"></span><span aria-label="Social link 3"></span><span aria-label="Social link 4"></span>
    </div>
  </div>
</div>

<header class="site-header wrap">
  <div class="brand">
    <div class="brand-name">The Hearth Guard Expert</div>
    <div class="brand-tag">Know Safety. Disaster Never Sleeps!</div>
  </div>
  <nav class="main-menu">
    <a class="active" href="#">Home</a>
    <a href="#">About Me</a>
    <a href="#">Safety Info &#8964;</a>
    <a href="http://www.rescueskillsnorthvale.example">Learn CPR</a>
    <a href="#">Prevent Home Disasters</a>
    <a href="#">Contact Me</a>
  </nav>
</header>

<section class="hero" role="img" aria-label="Firefighters on a ladder platform spraying a burning house at night">
  <div class="hero-text">
    <h1>Know Safety. Disaster Never Sleeps!</h1>
    <a class="btn-signup" href="#">SIGN UP NOW</a>
  </div>
</section>

<section class="intro wrap">
  <h2>Want to protect your home or loved one from an emergency ? Have you had a home emergency ? Not sure what to do ?</h2>
  <div class="intro-cols">
    <ul class="facts">
      <li>House Fires Kill 8 People every day.</li>
      <li>Flood damage accounts for $14.3 Billon in Property Damage Yearly.</li>
      <li>Disaster Never Sleeps and Always strikes at the Worst possible time.</li>
    </ul>
    <div class="intro-brand">
      <div class="mark"></div>
      <div class="name">The Hearth Guard Expert</div>
      <div class="tag">Know Safety. Disaster Never Sleeps!</div>
    </div>
    <ul class="promise">
      <li>Be Prepared. Know What to do.</li>
      <li>I am here for you.</li>
      <li>As an Emergency Services Professional I want to share what I have seen and how to Help.</li>
      <li>We all have busy lives. Preparing <b><i>NOW</i></b> will Save you Time, Money and could Save A Life.</li>
    </ul>
  </div>
</section>

<section class="safety">
  <h2><span>Safety</span> Info</h2>
  <div class="topics">
    <a class="topic" href="#"><div class="circle">
      <svg width="36" height="34" viewBox="0 0 36 34"><path d="M18 3 3 16h4v15h22V16h4z" fill="#fff"/><rect x="14" y="17" width="8" height="7" fill="#ec2227"/></svg>
    </div>Home Safety</a>
    <a class="topic" href="#"><div class="circle">
      <svg width="34" height="34" viewBox="0 0 34 34"><rect x="13" y="6" width="8" height="22" fill="#fff"/><rect x="6" y="13" width="22" height="8" fill="#fff"/></svg>
    </div>Life Safety</a>
    <a class="topic" href="#"><div class="circle">
      <svg width="24" height="38" viewBox="0 0 24 38"><rect x="6" y="10" width="12" height="26" rx="3" fill="#fff"/><rect x="9" y="5" width="6" height="5" fill="#fff"/><path d="M15 6h6v3" fill="none" stroke="#fff" stroke-width="2"/></svg>
    </div>Fire Safety</a>
    <a class="topic" href="#"><div class="circle">
      <svg width="38" height="28" viewBox="0 0 38 28"><path d="M4 16l5-9h20l5 9v8H4z" fill="#fff"/><circle cx="11" cy="24" r="3" fill="#ec2227"/><circle cx="27" cy="24" r="3" fill="#ec2227"/></svg>
    </div>Auto Safety</a>
    <a class="topic" href="#"><div class="circle">
      <svg width="36" height="34" viewBox="0 0 36 34"><path d="M18 3 3 16h4v15h22V16h4z" fill="none" stroke="#fff" stroke-width="3"/></svg>
    </div>Pet Safety</a>
  </div>
</section>

<section class="mailing wrap">
  <h2>Join My <span>Mailing List</span> Today !</h2>
  <p>Life gets busy. Don’t worry about having to check the site daily. Though, I would love it. Sign up today to receive a weekly update. This information will help in an emergency but can save you money and time too. Don’t miss out. Sign Up Today !</p>
  <form class="signup-form">
    <div class="field">First Name</div>
    <div class="field">Last Name</div>
    <div class="field">Email Address</div>
    <div class="btn-subscribe">SUBSCRIBE</div>
  </form>
</section>

<footer class="footer wrap">
  <nav class="footer-menu">
    <a href="#">Home</a><a href="#">About Me</a><a href="#">Safety Info</a><a href="http://www.rescueskillsnorthvale.example">Learn CPR</a><a href="#">Prevent Home Disasters</a><a href="#">Contact Me</a>
  </nav>
  <h3>Contact <span>Us</span></h3>
  <div class="contacts">
    <div class="contact"><span class="ico dark"><svg width="10" height="13" viewBox="0 0 10 13"><path d="M5 0a5 5 0 0 0-5 5c0 4 5 8 5 8s5-4 5-8a5 5 0 0 0-5-5z" fill="#fff"/><circle cx="5" cy="5" r="1.8" fill="#000"/></svg></span><span>123, building name,<br>City, Country</span></div>
    <div class="contact"><span class="ico"><svg width="12" height="12" viewBox="0 0 12 12"><path d="M2 1l2 0 1 3-1.5 1a7 7 0 0 0 3.5 3.5L8 7l3 1v2c0 1-1 1-1 1C5 11 1 7 1 2c0 0 0-1 1-1z" fill="#ec2227"/></svg></span><span>123 456 7890</span></div>
    <div class="contact"><span class="ico"><svg width="12" height="9" viewBox="0 0 12 9"><rect x=".5" y=".5" width="11" height="8" fill="none" stroke="#ec2227"/><path d="M.5.5 6 5l5.5-4.5" fill="none" stroke="#ec2227"/></svg></span><span>info@hearthguardexpert.example</span></div>
    <div class="contact"><span class="ico"><svg width="12" height="12" viewBox="0 0 12 12"><circle cx="6" cy="6" r="5.3" fill="none" stroke="#ec2227"/><ellipse cx="6" cy="6" rx="2.3" ry="5.3" fill="none" stroke="#ec2227"/><line x1=".7" y1="6" x2="11.3" y2="6" stroke="#ec2227"/></svg></span><span>www.hearthguardexpert<br>.example</span></div>
  </div>
</footer>

<div class="bottombar wrap">
  <div>© <b>The Hearth Guard Expert</b> - 2017. All Rights Reserved.</div>
  <div class="legal"><a href="#">Privacy Policy</a><a href="#">Disclaimers and Disclosures</a></div>
</div>

</body>
</html>
```